International Medical travel company needs professional card

We just purchased a logo through sketch nest, and now need a business card. We contract with Middle Eastern governments to bring patients who need complex medical care to the U.S. for treatment. We will upload logo. Titles, names, contact info, etc. needs to be in English on one side, Arabic on the other

Target Market(s)

Health administrators, professionals

Industry/Entity Type

Health Care

Contact Information for Business Card

logo on each side. Usual name/title/contact info

Font styles to use
Serif
Sans Serif

Colors
0255a3

Requirements
Must have
• English one side, Arabic the other

```html
<!DOCTYPE html>
<html lang="en">
<head>
<meta charset="utf-8">
<title>Vantage Care – Business Card</title>
<link rel="stylesheet" href="https://fonts.googleapis.com/css2?family=PT+Sans:wght@400&display=swap">
<style>
  :root {
    --page-bg: #3a3a3a;
    --card-bg: #222222;
    --brand-blue: #0255a3;
    --brand-gold: #c9c42a;
    --gold-dark: #9a961c;
    --text-light: #f2f2f2;
  }
  * { margin: 0; padding: 0; box-sizing: border-box; }
  html, body {
    width: 1105px;
    height: 1200px;
    overflow: hidden;
    background: var(--page-bg);
    font-family: "PT Sans", sans-serif;
  }
  .business-card {
    position: absolute;
    left: 52px;
    top: 316px;
    width: 1000px;
    height: 568px;
    background: var(--card-bg);
  }
  .contact-block {
    position: absolute;
    left: 50px;
    top: 44px;
    width: 350px;
  }
  .person-name {
    color: var(--brand-blue);
    font-size: 33px;
    line-height: 1;
    letter-spacing: 0.5px;
  }
  .person-title {
    color: var(--gold-dark);
    font-size: 24px;
    line-height: 1;
    margin-top: 14px;
  }
  .address {
    color: var(--text-light);
    font-size: 26px;
    line-height: 37px;
    margin-top: 20px;
  }
  .contact-list {
    list-style: none;
    color: var(--text-light);
    font-size: 26px;
    line-height: 37.5px;
  }
  .contact-list li {
    display: flex;
    align-items: center;
    gap: 14px;
    white-space: nowrap;
  }
  .contact-icon {
    width: 24px;
    height: 24px;
    flex: none;
    fill: var(--brand-blue);
  }
  .brand-wordmark {
    position: absolute;
    left: 48px;
    top: 398px;
    width: 350px;
    color: var(--brand-gold);
    font-size: 54px;
    line-height: 1;
    letter-spacing: 2px;
  }
  .brand-wordmark span { display: block; }
  .brand-frame {
    position: absolute;
    left: 415px;
    top: 59px;
    width: 520px;
    height: 444px;
    border: 11px solid var(--brand-gold);
    display: flex;
    align-items: center;
    justify-content: center;
  }
  .brand-frame-name {
    color: var(--brand-gold);
    font-size: 64px;
    line-height: 1;
    letter-spacing: 2px;
  }
</style>
</head>
<body>
  <section class="business-card">
    <div class="contact-block">
      <p class="person-name">ADAM REYES</p>
      <p class="person-title">CEO/FOUNDER</p>
      <p class="address">2140 Harbor Street<br>Juneau, Alaska 99801</p>
      <ul class="contact-list">
        <li>
          <svg class="contact-icon" viewBox="0 0 24 24" aria-hidden="true"><path d="M6.6 10.8a15.1 15.1 0 0 0 6.6 6.6l2.2-2.2c.3-.3.7-.4 1-.2 1.1.4 2.3.6 3.6.6.6 0 1 .4 1 1V20c0 .6-.4 1-1 1A17 17 0 0 1 3 4c0-.6.4-1 1-1h3.5c.6 0 1 .4 1 1 0 1.3.2 2.5.6 3.6.1.3 0 .7-.2 1z"/></svg>
          <span>907 555 0142</span>
        </li>
        <li>
          <svg class="contact-icon" viewBox="0 0 24 24" aria-hidden="true"><path d="M7 1h10a2 2 0 0 1 2 2v18a2 2 0 0 1-2 2H7a2 2 0 0 1-2-2V3a2 2 0 0 1 2-2zm0 3v14h10V4zm5 15.2a1.2 1.2 0 1 0 0 2.4 1.2 1.2 0 0 0 0-2.4z"/></svg>
          <span>907 555 0187</span>
        </li>
        <li>
          <svg class="contact-icon" viewBox="0 0 24 24" aria-hidden="true"><path d="M6 2h12v5H6zM4 8h16a2 2 0 0 1 2 2v7h-4v5H6v-5H2v-7a2 2 0 0 1 2-2zm4 7v5h8v-5z"/></svg>
          <span>907 555 0163</span>
        </li>
        <li>
          <svg class="contact-icon" viewBox="0 0 24 24" aria-hidden="true"><path d="M2 5h20v14H2zm2 2v.4l8 5 8-5V7zm0 2.8V17h16V9.8l-8 5z"/></svg>
          <span>hi@vantagecare.example</span>
        </li>
        <li>
          <svg class="contact-icon" viewBox="0 0 24 24" aria-hidden="true"><path d="M12 2a10 10 0 1 0 0 20 10 10 0 0 0 0-20zm-1 17.9A8 8 0 0 1 4.2 10L9 14.8v1.2c0 1.1.9 2 2 2zm6.9-2.5A2 2 0 0 0 16 16h-1v-3a1 1 0 0 0-1-1H8v-2h2a1 1 0 0 0 1-1V7h2a2 2 0 0 0 2-2v-.4a8 8 0 0 1 2.9 12.8z"/></svg>
          <span>www.vantagecare.example</span>
        </li>
      </ul>
    </div>

    <p class="brand-wordmark"><span>VANTAGE</span><span>CARE</span></p>

    <div class="brand-frame">
      <span class="brand-frame-name">VANTAGE CARE</span>
    </div>
  </section>
</body>
</html>
```